A New and modern Business Card for Talvern Contract Partners Ltd

New and modern Logo and Business Card Attached is the current logo/business card designCurrently the business is called "Talvern & Co." or TCP Ltd for short. This is subject to change.This business specialises in Telecoms and Energy. We work with the major networks (KX, V7, etc) and also offer Energy Products saving clients money off their energy bills.These are business to business services.The current design incorporates a Pheonix, indicating rebirth, starting something new.We would like to maintain the Phoenix element but a newer modern style.We love colours in the logo 3 max.The aim of this is to be ultra slick and modern. I envisage Talvern & Co. on one side of the card with long descriptions on the other side.Side 1:TCP Ltd/Logo?Side 2:TCP Ltd/Logo/Graphic?Brogan & Co.Name:Address:Phone:Email:The design is mostly flexible but must incorporate a Phoenix.For example "Talvern & Co." with a block phoenix behind the text...up to you.

Industry/Entity Type

Telecommunications

Contact Information for Business Card

Talvern & Co.
Address:
Name:
Phone:
Email:

Logo Text

Talvern & Co.

Colors
33a6d7
0792cd
acd037
9bcb3c
f78f20
fece3e

Requirements
Must have
• Phoenix
• 3/4 colours max
• Blue representing Technology (wireless)
• Green for Eco Energy
• Orange for Phoenix
• White business card background
Should not have
• phoenix must not all be red/ orange fire, we are a technology service company and the phoenix colours must represent this. Fire is not representative of our company.

```html
<!DOCTYPE html>
<html lang="en">
<head>
<meta charset="utf-8">
<title>Talvern Contract Partners Ltd — Business Card</title>
<link rel="stylesheet" href="https://fonts.googleapis.com/css2?family=Montserrat:wght@600;700&family=Roboto:wght@300&display=swap">
<style>
  :root {
    --page: #e9e7e4;
    --card-dark: #232222;
    --band-white: #f6f6f6;
    --band-grey: #bdbdbd;
    --brand-blue: #2f5ba3;
    --text-light: #f2f2f2;
  }
  * { box-sizing: border-box; margin: 0; padding: 0; }
  html, body { width: 1200px; height: 900px; overflow: hidden; }
  body {
    background: var(--page);
    display: flex;
    align-items: center;
    justify-content: center;
    gap: 40px;
    font-family: "Roboto", Arial, sans-serif;
  }
  .card {
    position: relative;
    width: 540px;
    height: 309px;
    background: var(--card-dark);
    box-shadow: 0 10px 28px rgba(0,0,0,.22);
    overflow: hidden;
  }

  /* Card back: company name */
  .card-back .wordmark {
    position: absolute;
    left: 0; right: 0; top: 118px;
    display: flex;
    align-items: center;
    justify-content: center;
    gap: 18px;
    color: var(--brand-blue);
    font-family: "Montserrat", Arial, sans-serif;
    font-weight: 600;
  }
  .wordmark .mark-dot {
    width: 46px; height: 46px;
    border-radius: 50%;
    background: var(--brand-blue);
  }
  .wordmark .name-main {
    display: block;
    font-size: 42px;
    letter-spacing: 7px;
    line-height: 1;
  }
  .wordmark .name-sub {
    display: block;
    font-size: 12px;
    letter-spacing: 2.6px;
    margin-top: 6px;
  }

  /* Card front: header band and contact details */
  .card-front .band { position: absolute; inset: 0; }
  .card-front .short-mark {
    position: absolute;
    left: 34px; top: 28px;
    display: flex;
    align-items: center;
    gap: 14px;
    color: var(--brand-blue);
    font-family: "Montserrat", Arial, sans-serif;
    font-weight: 700;
    font-size: 27px;
    letter-spacing: 1.5px;
  }
  .short-mark .mark-dot {
    width: 42px; height: 42px;
    border-radius: 50%;
    background: var(--brand-blue);
  }
  .holder-name {
    position: absolute;
    left: 0; right: 0; top: 148px;
    text-align: center;
    padding-left: 40px;
    color: var(--brand-blue);
    font-family: "Montserrat", Arial, sans-serif;
    font-weight: 700;
    font-size: 22px;
  }
  .contact {
    position: absolute;
    color: var(--text-light);
    font-weight: 300;
    font-size: 14px;
    letter-spacing: 2px;
    line-height: 1.55;
  }
  .contact-address { left: 24px; top: 204px; display: flex; gap: 12px; }
  .contact-lines { right: 30px; top: 226px; }
  .contact-row { display: flex; align-items: center; gap: 12px; }
  .icon { width: 16px; height: 16px; flex: none; fill: var(--text-light); }
</style>
</head>
<body>

  <section class="card card-back" aria-label="Business card back">
    <div class="wordmark">
      <span class="mark-dot"></span>
      <span>
        <span class="name-main">TALVERN</span>
        <span class="name-sub">Contract Partners Limited</span>
      </span>
    </div>
  </section>

  <section class="card card-front" aria-label="Business card front">
    <svg class="band" width="540" height="309" viewBox="0 0 540 309" aria-hidden="true">
      <rect x="0" y="0" width="540" height="108" fill="var(--band-grey)"/>
      <rect x="0" y="0" width="540" height="100" fill="var(--band-white)"/>
      <polygon points="250,108 274,108 262,122" fill="var(--band-grey)"/>
    </svg>

    <div class="short-mark">
      <span class="mark-dot"></span>
      <span>TCP Ltd</span>
    </div>

    <p class="holder-name">John doe</p>

    <div class="contact contact-address">
      <svg class="icon" viewBox="0 0 16 16" aria-hidden="true">
        <path d="M8 0a5.5 5.5 0 0 0-5.5 5.5C2.5 9.6 8 15 8 15s5.5-5.4 5.5-9.5A5.5 5.5 0 0 0 8 0zm0 8a2.5 2.5 0 1 1 0-5 2.5 2.5 0 0 1 0 5z"/>
      </svg>
      <p>Address and Location<br>street number 00000</p>
    </div>

    <div class="contact contact-lines">
      <p class="contact-row">
        <svg class="icon" viewBox="0 0 16 16" aria-hidden="true">
          <path d="M3.6 1l2.3 2.9-1.3 1.9c.9 2 2.5 3.6 4.5 4.6l1.9-1.3L14 11.4l-1.5 2.8C6.7 14.2 1.8 9.3 1.8 3.5z"/>
        </svg>
        +88 888 8888
      </p>
      <p class="contact-row">
        <svg class="icon" viewBox="0 0 16 16" aria-hidden="true">
          <path d="M1 3h14v10H1zM2 4.2v.3l6 4.3 6-4.3v-.3z"/>
        </svg>
        youremail@website.com
      </p>
    </div>
  </section>

</body>
</html>
```